Design my Display Ad! Product for Muscle Cramps -- Need Your Talent!

I need the PSD of a square display ad to be the design concept for other ad formats. The product is for leg and muscle cramps. The ad needs to encourage clicks, not simply impressions. Image should contain legs.

Visit www.velmoristride.com for a better idea of the product.

Target Market(s)

People age 55+ with leg cramps

Industry/Entity Type

Health And Wellness

Font styles to use
Sans Serif

Colors

Designer to choose colors to be used in the design.

Requirements
Must have
• One version with the text:
• The Real Cause of Leg Cramps
• Discover the Secret
• The other version with the text:
• Leg Cramps at Night
• Discover the Real Cause
• An image focused on legs.
• Attractive presentation -- this is a premium organic brand.
• Visit www.velmoristride.com for a better understanding of the product

```html
<!DOCTYPE html>
<html lang="en">
<head>
<meta charset="utf-8">
<title>Velmori Stride – Display Ad Set</title>
<link rel="stylesheet" href="https://fonts.googleapis.com/css2?family=Raleway:wght@500;600;700&display=swap">
<style>
  :root {
    --blue: #2aa6df;
    --blue-pale: #d6eef9;
    --lime: #a8cf38;
    --green-btn: #67a428;
    --grey-text: #5f5f5f;
    --frame: #39a9df;
    --white: #ffffff;
    --photo-light: #eef3ef;
    --photo-skin: #e8c3a8;
  }
  * { box-sizing: border-box; margin: 0; padding: 0; }
  html, body { width: 1200px; height: 1200px; overflow: hidden; background: var(--white); }
  body { font-family: "Raleway", sans-serif; }

  .stage {
    position: absolute; left: 0; top: 0;
    width: 1000px; height: 1000px;
    transform: scale(1.2); transform-origin: 0 0;
  }
  .ad {
    position: absolute; background: var(--white);
    border: 1px solid var(--frame); overflow: hidden;
  }
  .ad .hero { position: absolute; left: 0; top: 0; display: block; }
  .headline-small, .headline-big, .subline, .cta, .brand { position: absolute; }
  .headline-small { color: var(--blue); font-weight: 600; line-height: 1.2; text-transform: uppercase; }
  .headline-big { color: var(--blue); font-weight: 600; line-height: 1.05; text-transform: uppercase; }
  .subline { color: var(--grey-text); font-weight: 500; line-height: 1.05; }
  .cta {
    background: var(--green-btn); color: var(--white);
    font-weight: 700; text-transform: uppercase;
    display: flex; align-items: center; justify-content: center;
    border-radius: 2px;
  }
  .brand {
    color: var(--blue); font-weight: 700; text-transform: uppercase;
    text-align: center; line-height: 1.05;
  }
  .brand span { display: block; }
  .brand .brand-second { letter-spacing: 0.32em; }
  .center { left: 0; right: 0; text-align: center; }

  /* 300 x 600 */
  .ad-tall { left: 51px; top: 87px; width: 302px; height: 602px; }
  .ad-tall .headline-small { top: 285px; font-size: 24px; }
  .ad-tall .headline-big { top: 324px; font-size: 39px; }
  .ad-tall .subline { top: 381px; font-size: 19px; }
  .ad-tall .cta { left: 10px; top: 430px; width: 281px; height: 48px; font-size: 24px; }
  .ad-tall .brand { top: 515px; font-size: 34px; }
  .ad-tall .brand .brand-second { font-size: 19px; }

  /* 160 x 600 */
  .ad-sky { left: 366px; top: 85px; width: 162px; height: 603px; }
  .ad-sky .headline-small { top: 272px; font-size: 21px; }
  .ad-sky .headline-big { top: 336px; font-size: 34px; }
  .ad-sky .subline { top: 416px; font-size: 15px; }
  .ad-sky .cta { left: 6px; top: 455px; width: 149px; height: 47px; font-size: 19px; }
  .ad-sky .brand { top: 535px; font-size: 20px; }
  .ad-sky .brand .brand-second { font-size: 14px; }

  /* 300 x 250 */
  .ad-square { left: 561px; top: 85px; width: 302px; height: 252px; }
  .ad-square .headline-small { left: 6px; top: 116px; font-size: 17px; }
  .ad-square .headline-big { left: 5px; top: 138px; font-size: 27px; }
  .ad-square .subline { left: 7px; top: 170px; font-size: 18px; }
  .ad-square .cta { left: 7px; top: 201px; width: 124px; height: 45px; font-size: 17px; }
  .ad-square .brand { left: 146px; top: 196px; width: 152px; font-size: 21px; }
  .ad-square .brand .brand-second { font-size: 13px; }

  /* 728 x 90 */
  .ad-leader { left: 51px; top: 721px; width: 730px; height: 92px; }
  .ad-leader .headline-small { left: 191px; top: 11px; font-size: 21px; }
  .ad-leader .headline-big { left: 190px; top: 43px; font-size: 34px; }
  .ad-leader .subline { left: 440px; top: 5px; width: 115px; text-align: center; font-size: 17px; }
  .ad-leader .cta { left: 421px; top: 45px; width: 154px; height: 43px; font-size: 19px; }
  .ad-leader .brand { left: 582px; top: 25px; width: 146px; font-size: 21px; }
  .ad-leader .brand .brand-second { font-size: 13px; }
</style>
</head>
<body>
<main class="stage">

  <section class="ad ad-tall">
    <svg class="hero" width="302" height="260" viewBox="0 0 302 260" role="img" aria-label="Photo of a woman's legs as she gently massages her calf, on a soft bright background">
      <defs>
        <linearGradient id="photo-tall" x1="0" y1="0" x2="1" y2="1">
          <stop offset="0" stop-color="var(--photo-light)"/>
          <stop offset="0.55" stop-color="#f0ddd0"/>
          <stop offset="1" stop-color="var(--photo-skin)"/>
        </linearGradient>
      </defs>
      <polygon points="0,0 302,0 302,165 235,252 0,152" fill="url(#photo-tall)"/>
      <polygon points="0,152 0,232 230,215 140,190" fill="var(--lime)"/>
      <polygon points="302,165 302,212 262,214" fill="var(--lime)"/>
      <polyline points="0,150 235,252 302,165" fill="none" stroke="var(--blue-pale)" stroke-width="4"/>
    </svg>
    <p class="headline-small center">The Real Cause of</p>
    <h2 class="headline-big center">Leg Cramps</h2>
    <p class="subline center">Discover the Secret</p>
    <a class="cta">Learn More</a>
    <div class="brand center"><span>Velmori</span><span class="brand-second">Stride</span></div>
  </section>

  <section class="ad ad-sky">
    <svg class="hero" width="162" height="260" viewBox="0 0 162 260" role="img" aria-label="Photo of bent legs with a hand resting on the knee">
      <defs>
        <linearGradient id="photo-sky" x1="0" y1="0" x2="1" y2="1">
          <stop offset="0" stop-color="#edd2c1"/>
          <stop offset="0.6" stop-color="var(--photo-skin)"/>
          <stop offset="1" stop-color="#f6eee8"/>
        </linearGradient>
      </defs>
      <polygon points="0,0 162,0 162,205 125,252 0,200" fill="url(#photo-sky)"/>
      <polygon points="0,200 0,243 100,240" fill="var(--lime)"/>
      <polygon points="162,205 162,235 140,236" fill="var(--lime)"/>
      <polyline points="0,198 125,254 162,205" fill="none" stroke="var(--blue-pale)" stroke-width="4"/>
    </svg>
    <p class="headline-small center">The Real<br>Cause of</p>
    <h2 class="headline-big center">Leg<br>Cramps</h2>
    <p class="subline center">Discover the Secret</p>
    <a class="cta">Learn More</a>
    <div class="brand center"><span>Velmori</span><span class="brand-second">Stride</span></div>
  </section>

  <section class="ad ad-square">
    <svg class="hero" width="302" height="130" viewBox="0 0 302 130" role="img" aria-label="Photo of a woman's legs with hands massaging the calf">
      <defs>
        <linearGradient id="photo-square" x1="0" y1="0" x2="1" y2="1">
          <stop offset="0" stop-color="var(--photo-light)"/>
          <stop offset="0.55" stop-color="#f0ddd0"/>
          <stop offset="1" stop-color="var(--photo-skin)"/>
        </linearGradient>
      </defs>
      <polygon points="0,0 302,0 302,45 232,127 0,48" fill="url(#photo-square)"/>
      <polygon points="0,48 0,92 150,98" fill="var(--lime)"/>
      <polygon points="302,45 302,78 265,84" fill="var(--lime)"/>
      <polyline points="0,46 232,128 302,45" fill="none" stroke="var(--blue-pale)" stroke-width="3"/>
    </svg>
    <p class="headline-small">The Real Cause of</p>
    <h2 class="headline-big">Leg Cramps</h2>
    <p class="subline">Discover the Secret</p>
    <a class="cta">Learn More</a>
    <div class="brand"><span>Velmori</span><span class="brand-second">Stride</span></div>
  </section>

  <section class="ad ad-leader">
    <svg class="hero" width="190" height="92" viewBox="0 0 190 92" role="img" aria-label="Photo of a woman's leg raised with a hand on the calf">
      <defs>
        <linearGradient id="photo-leader" x1="0" y1="0" x2="1" y2="0">
          <stop offset="0" stop-color="#f7efe9"/>
          <stop offset="0.5" stop-color="var(--photo-skin)"/>
          <stop offset="1" stop-color="#f7efe9"/>
        </linearGradient>
      </defs>
      <polygon points="0,0 160,0 182,10 158,92 0,92" fill="url(#photo-leader)"/>
      <polygon points="165,0 178,0 160,92 150,92" fill="var(--lime)"/>
      <polyline points="160,0 185,10 160,92" fill="none" stroke="var(--blue-pale)" stroke-width="3"/>
    </svg>
    <p class="headline-small">The Real Cause of</p>
    <h2 class="headline-big">Leg Cramps</h2>
    <p class="subline">Discover the Secret</p>
    <a class="cta">Learn More</a>
    <div class="brand"><span>Velmori</span><span class="brand-second">Stride</span></div>
  </section>

</main>
</body>
</html>
```